Harlow Pantry Co makers of various food product lines for Australian market

We need a label design concept for various product lines , this concept should have common elements across the lines. The labels within the lines would need to be specific to the individual products. The initial product lines will include the following, Sauces (mild to very hot) , Meat products, dried and fresh (Biltong to Boerewors) and also ready prepared uncooked meat products (marinated chicken portions, chicken wings etc). The target customers will be in two categories. Firstly, individuals (often ex South African residents) looking to purchase the specific sauces and meat products in smaller portion packaging. Second, distribution to select restaurants and pubs , different products to specific business types. ie bulk sauces and prepared products to restaurants and Biltong type products to pubs for snacks etc. The products currently being made are Portuguese style Peri Peri sauce (mild, original) , Peri Peri sauce (hot with Habanero chillies) and Biltong (dried meat snack similar to Jerky). The sauces are being sold to friends and family and word of mouth customers in hand labeled 240 ml bottles , the Biltong is sold via a Facebook group and word of mouth customers with very basic labels onto brown paper packets. We will be marketing the products as current, as well as Farmers markets and direct contact with selected restaurants and pubs. The products are made using traditional recipes and methods. Proposed label size 64mm h x 108 mm w. The theme should have a slightly rustic African feel to it.

```html
<!DOCTYPE html>
<html lang="en">
<head>
<meta charset="utf-8">
<title>Tobi's ember sauce – peri peri label range</title>
<link href="https://fonts.googleapis.com/css2?family=Montserrat:wght@400;500;700&display=swap" rel="stylesheet">
<style>
  :root {
    --bg: #ffffff;
    --label: #ffffff;
    --ink: #1c1c1c;
    --brand-red: #c4262e;
    --muted: #555555;
    --rule: #bdbdbd;
    --pattern-a: #b8232b;
    --pattern-b: #e9782a;
    --pattern-c: #2e2a2a;
    --edge: #e2e2e2;
  }
  * { margin: 0; padding: 0; box-sizing: border-box; }
  html, body {
    width: 789px; height: 1200px; overflow: hidden;
    background: var(--bg);
    font-family: "Montserrat", sans-serif;
    color: var(--ink);
  }
  .range { position: relative; width: 789px; height: 1200px; }
  .label {
    position: absolute;
    width: 320px; height: 280px;
    background: var(--label);
    border: 1px solid var(--edge);
    display: flex;
  }
  .label--one { left: 50px; top: 170px; }
  .label--original { left: 420px; top: 170px; }
  .label--two { left: 50px; top: 725px; }
  .label--three { left: 420px; top: 725px; }

  .label__pattern {
    width: 92px; height: 100%;
    background: linear-gradient(180deg, var(--pattern-a) 0%, var(--pattern-b) 35%, var(--pattern-c) 55%, var(--pattern-a) 80%, var(--pattern-b) 100%);
    flex-shrink: 0;
  }
  .label__body { position: relative; flex: 1; padding: 16px 14px 12px 16px; }
  .label__brand { font-size: 15px; font-weight: 700; color: var(--brand-red); line-height: 1; }
  .label__line {
    font-size: 21px; font-weight: 400; line-height: 1.05;
    margin-top: 14px;
    border-bottom: 1px solid var(--rule);
    padding-bottom: 8px;
    width: 150px;
  }
  .label__product { display: flex; align-items: flex-end; margin-top: 8px; }
  .label__name { font-size: 44px; font-weight: 500; line-height: 0.86; letter-spacing: -1px; }
  .label__heat { font-size: 40px; font-weight: 400; line-height: 0.9; margin-left: 4px; }
  .label__desc { font-size: 10.5px; line-height: 1.3; color: var(--muted); margin-top: 12px; width: 140px; }
  .label__mark {
    position: absolute; right: 20px; top: 172px;
    width: 20px; height: 20px;
    background: var(--ink);
  }
  .label__foot { position: absolute; left: 16px; bottom: 12px; font-size: 8px; color: var(--muted); }
</style>
</head>
<body>
<main class="range">

  <article class="label label--one">
    <div class="label__pattern" role="img" aria-label="Vertical band of African zigzag diamond pattern"></div>
    <div class="label__body">
      <p class="label__brand">Tobi's</p>
      <p class="label__line">ember<br>sauce</p>
      <div class="label__product"><span class="label__name">peri<br>peri</span><span class="label__heat">1</span></div>
      <p class="label__desc">Contains the world's hottest pepper Carolina Reaper</p>
      <div class="label__mark" role="img" aria-label="Small origin mark"></div>
      <p class="label__foot">small batch</p>
    </div>
  </article>

  <article class="label label--original">
    <div class="label__pattern" role="img" aria-label="Vertical band of African zigzag diamond pattern"></div>
    <div class="label__body">
      <p class="label__brand">Tobi's</p>
      <p class="label__line">ember<br>sauce</p>
      <div class="label__product"><span class="label__name">peri<br>peri</span></div>
      <p class="label__desc">Original Recipe with African Bird's Eye pepper</p>
      <div class="label__mark" role="img" aria-label="Small origin mark"></div>
      <p class="label__foot">small batch</p>
    </div>
  </article>

  <article class="label label--two">
    <div class="label__pattern" role="img" aria-label="Vertical band of African zigzag diamond pattern"></div>
    <div class="label__body">
      <p class="label__brand">Tobi's</p>
      <p class="label__line">ember<br>sauce</p>
      <div class="label__product"><span class="label__name">peri<br>peri</span><span class="label__heat">2</span></div>
      <p class="label__desc">With the very very hot Trinidad Moruga Scorpion pepper</p>
      <div class="label__mark" role="img" aria-label="Small origin mark"></div>
      <p class="label__foot">small batch</p>
    </div>
  </article>

  <article class="label label--three">
    <div class="label__pattern" role="img" aria-label="Vertical band of African zigzag diamond pattern"></div>
    <div class="label__body">
      <p class="label__brand">Tobi's</p>
      <p class="label__line">ember<br>sauce</p>
      <div class="label__product"><span class="label__name">peri<br>peri</span><span class="label__heat">3</span></div>
      <p class="label__desc">With the very hot Red Savina Habanero pepper</p>
      <div class="label__mark" role="img" aria-label="Small origin mark"></div>
      <p class="label__foot">small batch</p>
    </div>
  </article>

</main>
</body>
</html>
```